Holiday Rental Company Flyer Design (DL not A5)

Note from PixelFolk Administration: The category sizing selected is A5, however the project requires DL sized artwork. Please refer to the DL template link below while the 'Special Requirements' are updated accordingly.

Project Brief:
We need a double sided DL flyer designed for an up market Holiday Rental Company that portrays a personalised approach to property management. These are to be used for letter box drops to homes we're specifically targeting so the design should be modern, complimentary colour palette, uncluttered & visually appealing.

Please Download the DL Template from Quillmark here: http://www.quillmark.com.au/qm/ns/propath/UploadResources.aspx?selectedTab=0?pfid=BFB&pf_id=BFB&xnav=easypath-upload-image#Templates

Target Market(s)

Wealthy Home Owners

Industry/Entity Type

It Company

Font styles to use
Other font styles liked:
• Avant Garde Extra Light & Demi

Colors
33b8a4

Requirements
Must have
• DL Flyer sizes (210mm width x 99mm width, plus 3mm bleed)
• Front: Logo, Main Image & Grab
• Back: Contact Details & Brief Description of our business
• Images: Ideally the main image should be the house with the pool but alternatively a lifestyle images could also be used.
Nice to have
• A creative designer!
Should not have
• Clutter & busy designs

```html
<!DOCTYPE html>
<html lang="en">
<head>
<meta charset="utf-8">
<title>Holiday Rental Flyer – Front</title>
<link rel="stylesheet" href="https://fonts.googleapis.com/css2?family=Poppins:wght@200;300;600&display=swap">
<style>
  :root {
    --backdrop: #3b3b3d;
    --teal: #33b8a4;
    --teal-light: #3fc4af;
    --night-sky: #2a2370;
    --dusk-violet: #6a55b8;
    --lamp-gold: #c9a46a;
    --pool-blue: #1f7fe0;
    --pool-deep: #0f5fc4;
    --white: #ffffff;
  }
  * { margin: 0; padding: 0; box-sizing: border-box; }
  html, body {
    width: 1200px;
    height: 870px;
    overflow: hidden;
    background: var(--backdrop);
  }
  .flyer {
    position: absolute;
    left: 50px;
    top: 175px;
    width: 1100px;
    height: 519px;
    overflow: hidden;
    font-family: "Poppins", sans-serif;
    color: var(--white);
  }
  .flyer__photo {
    position: absolute;
    inset: 0;
    background:
      linear-gradient(180deg, transparent 0%, transparent 70%, var(--pool-blue) 78%, var(--pool-deep) 100%),
      radial-gradient(ellipse 40% 30% at 42% 58%, rgba(230, 190, 120, 0.85), transparent 70%),
      linear-gradient(180deg, var(--night-sky) 0%, #3d3290 30%, var(--dusk-violet) 55%, #4a3f7a 70%);
  }
  .flyer__panel {
    position: absolute;
    inset: 0;
  }
  .brand {
    position: absolute;
    left: 56px;
    bottom: 60px;
    display: flex;
    align-items: center;
    gap: 18px;
  }
  .brand__name {
    font-weight: 200;
    font-size: 30px;
    line-height: 1.1;
    letter-spacing: 0.22em;
    text-transform: uppercase;
    color: var(--white);
  }
  .brand__mark {
    width: 34px;
    height: 34px;
    border: 1px solid var(--white);
    border-radius: 50%;
  }
  .headline {
    position: absolute;
    right: 44px;
    bottom: 130px;
    text-align: left;
  }
  .headline__title {
    font-weight: 600;
    font-size: 58px;
    line-height: 1;
    letter-spacing: 0.01em;
  }
  .headline__tagline {
    font-weight: 200;
    font-size: 27px;
    line-height: 1.3;
    letter-spacing: 0.04em;
  }
</style>
</head>
<body>
  <section class="flyer">
    <div class="flyer__photo" role="img" aria-label="Night photograph of a modern two-storey holiday home with lit windows beside a glowing blue pool under a violet sky"></div>

    <svg class="flyer__panel" viewBox="0 0 1100 519" preserveAspectRatio="none" aria-hidden="true">
      <defs>
        <linearGradient id="tealFacet" x1="0" y1="0" x2="1" y2="1">
          <stop offset="0" stop-color="#3fc4af"/>
          <stop offset="1" stop-color="#33b8a4"/>
        </linearGradient>
      </defs>
      <polygon points="0,0 400,0 0,519" fill="url(#tealFacet)"/>
      <polygon points="0,0 400,0 140,200" fill="#ffffff" opacity="0.05"/>
    </svg>

    <div class="brand">
      <div class="brand__name">Harbourline<br>Retreats</div>
      <span class="brand__mark"></span>
    </div>

    <div class="headline">
      <h1 class="headline__title">Holiday Rental</h1>
      <p class="headline__tagline">Management with a difference</p>
    </div>
  </section>
</body>
</html>
```